Managed IT services business card design

We haven't needed a business card since the founding of the business in 2005. All our clients have been coming through word of mouth. And lately more and more existing clients are requesting for our business cards to pass on to their contacts in recommending us.
So we needing a business card design. We use various innovative solutions and methodologies to provide IT services to small businesses in managing their IT systems. Our role is the same as an in-house, full-time IT Manager for our clients, but outsourced. So we take care of all our clients' IT needs, just as an IT Manager would be expected to perform.
We have a holding website, which we're happy to leave for now. If we can use the same logo would be great - www.lomvex.com.au
Preferred colours are shades of are white, grey and black.
We pride our business with the following traits: proactive, good service, prompt response, trustworthy.
Target Market(s)
Small businesses of any industry
Industry/Entity Type
Business

```html
<!DOCTYPE html>
<html lang="en">
<head>
<meta charset="utf-8">
<title>lomvex business card</title>
<link rel="stylesheet" href="https://fonts.googleapis.com/css2?family=Open+Sans:wght@400;600&display=swap">
<style>
  :root {
    --page-bg: #2a2a2c;
    --card-white: #ffffff;
    --card-black: #0a0b0d;
    --card-black-soft: #1d1f23;
    --silver-light: #f4f4f4;
    --silver-mid: #b9bbbe;
    --silver-dark: #6f7276;
    --logo-ink: #111111;
    --name-grey: #8e9093;
    --text-white: #f2f2f2;
    --icon-grey: #d6d6d6;
  }
  * { margin: 0; padding: 0; box-sizing: border-box; }
  html, body {
    width: 1200px; height: 800px; overflow: hidden;
    background: var(--page-bg);
    font-family: "Open Sans", Arial, sans-serif;
  }
  .card {
    position: absolute; left: 160px; top: 130px;
    width: 880px; height: 540px;
    border-radius: 4px; overflow: hidden;
    box-shadow: 0 18px 40px rgba(0,0,0,0.45);
    background: var(--card-black);
  }
  .card__top {
    position: absolute; left: 0; top: 0; right: 0; height: 200px;
    background: var(--card-white);
  }
  .card__band {
    position: absolute; left: 0; right: 0; top: 200px; height: 14px;
    background: linear-gradient(180deg, var(--silver-light) 0%, var(--silver-mid) 45%, var(--silver-dark) 100%);
  }
  .card__texture {
    position: absolute; left: 0; right: 0; top: 214px; bottom: 0;
    background: linear-gradient(165deg, var(--card-black-soft) 0%, #131519 45%, var(--card-black) 100%);
  }
  .brand-name {
    position: absolute; left: 80px; top: 104px;
    font-weight: 400; font-size: 64px; line-height: 1;
    color: var(--logo-ink);
  }
  .contact {
    position: absolute; left: 80px; top: 230px;
    color: var(--text-white);
  }
  .contact__name {
    font-weight: 400; font-size: 28px; line-height: 1.1;
    color: var(--name-grey);
  }
  .contact__role {
    font-weight: 600; font-size: 16px; line-height: 1.4;
    margin: 2px 0 12px 16px;
  }
  .contact__list { list-style: none; margin-left: 32px; }
  .contact__item {
    display: flex; align-items: center; gap: 10px;
    font-size: 22px; line-height: 31px;
  }
  .contact__item--cont { padding-left: 32px; }
  .contact__icon { width: 22px; height: 22px; flex: none; fill: var(--icon-grey); }
</style>
</head>
<body>
  <main class="card">
    <div class="card__top"></div>
    <div class="card__band"></div>
    <div class="card__texture" role="img" aria-label="Fine dotted dark texture"></div>

    <div class="brand-name">lomvex</div>

    <section class="contact">
      <p class="contact__name">Firstname Lastname</p>
      <p class="contact__role">manager</p>
      <ul class="contact__list">
        <li class="contact__item">
          <svg class="contact__icon" viewBox="0 0 24 24" aria-hidden="true"><path d="M6.6 10.8a15 15 0 0 0 6.6 6.6l2.2-2.2c.3-.3.7-.4 1-.2 1.1.4 2.3.6 3.6.6.6 0 1 .4 1 1V20c0 .6-.4 1-1 1C10.6 21 3 13.4 3 4c0-.6.4-1 1-1h3.5c.6 0 1 .4 1 1 0 1.3.2 2.5.6 3.6.1.3 0 .7-.2 1z"/></svg>
          <span>02 9470 3186</span>
        </li>
        <li class="contact__item">
          <svg class="contact__icon" viewBox="0 0 24 24" aria-hidden="true"><path d="M7 3h10v4H7zM4 8h16a2 2 0 0 1 2 2v6h-4v5H6v-5H2v-6a2 2 0 0 1 2-2zm4 8v3h8v-3z"/></svg>
          <span>02 9470 3187</span>
        </li>
        <li class="contact__item">
          <svg class="contact__icon" viewBox="0 0 24 24" aria-hidden="true"><path d="M3 5h18v14H3zm2 2v.4l7 5 7-5V7zm0 2.8V17h14V9.8l-7 5z"/></svg>
          <span>info@www.lomvex.com.au</span>
        </li>
        <li class="contact__item">
          <svg class="contact__icon" viewBox="0 0 24 24" aria-hidden="true"><path d="M12 2a10 10 0 1 0 0 20 10 10 0 0 0 0-20zm7.9 9h-3.4a15 15 0 0 0-1.3-6.1A8 8 0 0 1 19.9 11zM12 4c.9 1.2 2.2 3.7 2.5 7h-5C9.8 7.7 11.1 5.2 12 4zM8.8 4.9A15 15 0 0 0 7.5 11H4.1a8 8 0 0 1 4.7-6.1zM4.1 13h3.4a15 15 0 0 0 1.3 6.1A8 8 0 0 1 4.1 13zM12 20c-.9-1.2-2.2-3.7-2.5-7h5c-.3 3.3-1.6 5.8-2.5 7zm3.2-.9a15 15 0 0 0 1.3-6.1h3.4a8 8 0 0 1-4.7 6.1z"/></svg>
          <span>www.lomvex.com.au</span>
        </li>
        <li class="contact__item">
          <svg class="contact__icon" viewBox="0 0 24 24" aria-hidden="true"><path d="M12 3l10 9h-3v9h-5v-6h-4v6H5v-9H2z"/></svg>
          <span>17 Harlow Street Minto</span>
        </li>
        <li class="contact__item contact__item--cont">
          <span>NSW 2566, Sydney</span>
        </li>
      </ul>
    </section>
  </main>
</body>
</html>
```